Leadership Brenvale Brochure Design*

We host a local leadership development program every two years. We need a brochure to promote the program. We would like it to be 8 1/2 x 11, tri-fold. I have attached a Word document with the necessary info for the brochure. The brochure will be professionally printed. We would like the final design to be in InDesign.

Target Market(s)

Potential participants of our leadership program. They will be local leaders, male and female, from 30-60 years of age.

Requirements
Must have
• Content as detailed in the Word document attached. Our logo.
Nice to have
• A design that is attractive to young professionals.

```html
<!DOCTYPE html>
<html lang="en">
<head>
<meta charset="utf-8">
<title>Leadership Brenvale – Program Overview</title>
<link rel="stylesheet" href="https://fonts.googleapis.com/css2?family=Open+Sans:wght@400;600;700&display=swap">
<style>
:root{
  --navy:#2e3583;
  --blue:#0a8fd8;
  --sky:#1a8ad4;
  --green:#8dc63f;
  --orange:#f5861f;
  --card:#dcdde0;
  --ink:#222;
  --page:#e9e9ea;
}
*{box-sizing:border-box;margin:0;padding:0}
html,body{width:1200px;height:1000px;overflow:hidden;background:var(--page)}
body{font-family:"Open Sans",Arial,sans-serif;color:var(--ink);position:relative}
.spread{position:absolute;left:80px;top:88px;width:1040px;height:804px;background:#fff;overflow:hidden}
.spread-bg{position:absolute;left:0;top:0}
.abs{position:absolute}
.header-icon{left:46px;top:33px;width:34px;height:34px;border-radius:50%;background:#fff}
.header-title{left:94px;top:39px;color:#fff;font-weight:700;font-size:16px}
.body-text{font-size:10.6px;line-height:18.4px;letter-spacing:-0.05px}
.intro{left:46px;top:83px;width:276px}
.goal{position:absolute;left:46px;width:280px;padding-left:41px;font-size:10.6px;line-height:18.4px}
.goal .box{position:absolute;left:1px;width:22px;height:22px;background:var(--blue);border-radius:2px}
.schedule-tag{left:46px;top:399px;width:142px;height:24px;background:var(--navy);border-radius:12px 0 12px 0;color:#fff;font-weight:700;font-size:15px;padding-left:51px;line-height:24px}
.schedule-tag svg{position:absolute;left:22px;top:3px}
.card{position:absolute;width:274px;background:var(--card);border-radius:0 0 26px 0}
.card-title{position:absolute;left:0;z-index:1;background:var(--blue);color:#fff;font-weight:700;font-size:10.8px;line-height:15.5px;padding:2px 12px;width:237px}
.card-date{position:absolute;right:7px;z-index:2;width:77px;height:20px;background:var(--green);color:#fff;font-size:10.8px;line-height:20px;padding-left:11px;border-radius:0 8px 0 8px}
.card-time{position:absolute;left:14px;width:170px;height:25px;background:var(--navy);border-radius:0 0 10px 0;color:#fff;font-size:10.8px;line-height:25px;padding-left:42px}
.card-time svg{position:absolute;left:13px;top:1px}
.card-list{position:absolute;left:14px;list-style:none}
.card-list li{position:relative;padding-left:19px;font-size:10.6px;line-height:18.4px}
.card-list li svg{position:absolute;left:0;top:5px}
.side-head{position:absolute;left:719px;color:var(--sky);font-weight:700;font-size:12.5px}
.side-text{position:absolute;left:719px;width:280px}
.phone{left:721px;top:698px;font-size:10.6px;line-height:16px}
.phone-num{left:721px;top:714px;font-weight:700;font-size:13px;color:var(--navy);padding-left:20px;line-height:18px}
.phone-num svg{position:absolute;left:0;top:2px}
</style>
</head>
<body>
<div class="spread">
  <svg class="spread-bg" width="1040" height="804" viewBox="0 0 1040 804">
    <path d="M430,64 C650,50 900,40 1040,40 V215 C1000,150 900,95 700,80 C600,72 500,68 430,64 Z" fill="var(--orange)"/>
    <path d="M0,0 H1040 V40 C900,44 700,50 500,62 C300,72 150,80 0,90 Z" fill="var(--navy)"/>
    <path d="M0,745 C400,778 700,760 1040,684 V804 H0 Z" fill="var(--green)"/>
    <path d="M0,757 C350,786 750,762 1040,712 V804 H0 Z" fill="var(--blue)"/>
  </svg>

  <div class="abs header-icon">
    <svg width="34" height="34" viewBox="0 0 34 34">
      <circle cx="17" cy="17" r="14" fill="none" stroke="var(--blue)" stroke-width="2"/>
      <circle cx="17" cy="11" r="3" fill="var(--navy)"/>
      <circle cx="11" cy="20" r="2.6" fill="var(--blue)"/>
      <circle cx="23" cy="20" r="2.6" fill="var(--blue)"/>
      <path d="M8,26 q3,-4 6,0 M20,26 q3,-4 6,0 M14,17 q3,-4 6,0" stroke="var(--navy)" stroke-width="2" fill="none"/>
    </svg>
  </div>
  <div class="abs header-title">Program Overview</div>

  <p class="abs body-text intro">Leadership Brenvale is a leadership certification program designed to prepare the leaders of tomorrow. During the five-month program, participants get an in-depth view of community issues, develop leadership skills necessary to assume leadership roles, and are exposed to community involvement opportunities. Leadership Brenvale will provide participants with the opportunities to:</p>

  <div class="goal" style="top:241px"><span class="box" style="top:9px"><svg width="22" height="22" viewBox="0 0 22 22"><path d="M5,11 l4,4 l8,-9" stroke="#fff" stroke-width="2.2" fill="none"/></svg></span>Build and demonstrate leadership and<br>communication skills</div>
  <div class="goal" style="top:282px"><span class="box" style="top:6px"><svg width="22" height="22" viewBox="0 0 22 22"><path d="M5,11 l4,4 l8,-9" stroke="#fff" stroke-width="2.2" fill="none"/></svg></span>Think critically about key business, policy, and<br>civic issues facing Brenvale County</div>
  <div class="goal" style="top:323px"><span class="box" style="top:0"><svg width="22" height="22" viewBox="0 0 22 22"><path d="M5,11 l4,4 l8,-9" stroke="#fff" stroke-width="2.2" fill="none"/></svg></span>Build meaningful, long-lasting connections</div>
  <div class="goal" style="top:349px"><span class="box" style="top:8px"><svg width="22" height="22" viewBox="0 0 22 22"><path d="M5,11 l4,4 l8,-9" stroke="#fff" stroke-width="2.2" fill="none"/></svg></span>Establish ongoing dialogues with experienced<br>community leaders</div>

  <div class="abs schedule-tag">
    <svg width="20" height="18" viewBox="0 0 20 18"><rect x="1" y="2" width="14" height="13" rx="2" fill="var(--orange)"/><circle cx="14" cy="12" r="5" fill="#fff" stroke="var(--orange)" stroke-width="1.5"/><path d="M14,9.5 V12 H16" stroke="var(--orange)" stroke-width="1.3" fill="none"/></svg>
    Schedule:
  </div>

  <!-- Organizational Retreat -->
  <div class="card" style="left:46px;top:434px;height:176px">
    <div class="card-date" style="top:-6px">January 17</div>
    <div class="card-title" style="top:-1px;width:236px">Organizational Retreat &amp; Dinner<br>(Attendance Mandatory)</div>
    <div class="card-time" style="top:44px">
      <svg width="22" height="22" viewBox="0 0 22 22"><circle cx="11" cy="11" r="10" fill="#fff"/><circle cx="11" cy="11" r="7.5" fill="none" stroke="var(--blue)" stroke-width="2"/><path d="M11,6.5 V11 H14" stroke="var(--navy)" stroke-width="1.6" fill="none"/></svg>
      10:00 a.m. – 7:00 p.m.
    </div>
    <ul class="card-list" style="top:75px">
      <li><svg width="12" height="11" viewBox="0 0 12 11"><path d="M1,6 l3.5,3.5 l6.5,-8" stroke="#111" stroke-width="2" fill="none"/></svg>Introductions</li>
      <li><svg width="12" height="11" viewBox="0 0 12 11"><path d="M1,6 l3.5,3.5 l6.5,-8" stroke="#111" stroke-width="2" fill="none"/></svg>Team Building</li>
      <li><svg width="12" height="11" viewBox="0 0 12 11"><path d="M1,6 l3.5,3.5 l6.5,-8" stroke="#111" stroke-width="2" fill="none"/></svg>Motivation</li>
      <li><svg width="12" height="11" viewBox="0 0 12 11"><path d="M1,6 l3.5,3.5 l6.5,-8" stroke="#111" stroke-width="2" fill="none"/></svg>Leadership Styles</li>
      <li><svg width="12" height="11" viewBox="0 0 12 11"><path d="M1,6 l3.5,3.5 l6.5,-8" stroke="#111" stroke-width="2" fill="none"/></svg>Social Hour/Dinner</li>
    </ul>
  </div>

  <!-- Business & Industry -->
  <div class="card" style="left:46px;top:627px;height:133px">
    <div class="card-date" style="top:-7px">January 31</div>
    <div class="card-title" style="top:3px">Business &amp; Industry</div>
    <div class="card-time" style="top:22px">
      <svg width="22" height="22" viewBox="0 0 22 22"><circle cx="11" cy="11" r="10" fill="#fff"/><circle cx="11" cy="11" r="7.5" fill="none" stroke="var(--blue)" stroke-width="2"/><path d="M11,6.5 V11 H14" stroke="var(--navy)" stroke-width="1.6" fill="none"/></svg>
      8:30 a.m. – 4:00 p.m
    </div>
    <ul class="card-list" style="top:52px">
      <li><svg width="12" height="11" viewBox="0 0 12 11"><path d="M1,6 l3.5,3.5 l6.5,-8" stroke="#111" stroke-width="2" fill="none"/></svg>Business &amp; Industry Panel</li>
      <li><svg width="12" height="11" viewBox="0 0 12 11"><path d="M1,6 l3.5,3.5 l6.5,-8" stroke="#111" stroke-width="2" fill="none"/></svg>Tour of Ironvale Manufacturing facility</li>
      <li><svg width="12" height="11" viewBox="0 0 12 11"><path d="M1,6 l3.5,3.5 l6.5,-8" stroke="#111" stroke-width="2" fill="none"/></svg>Tour of Garrick Tool Company</li>
      <li><svg width="12" height="11" viewBox="0 0 12 11"><path d="M1,6 l3.5,3.5 l6.5,-8" stroke="#111" stroke-width="2" fill="none"/></svg>“Taking your vision into B&amp;I”</li>
    </ul>
  </div>

  <!-- Education -->
  <div class="card" style="left:383px;top:88px;height:171px">
    <div class="card-date" style="top:-6px">February 21</div>
    <div class="card-title" style="top:2px">Education</div>
    <div class="card-time" style="top:21px">
      <svg width="22" height="22" viewBox="0 0 22 22"><circle cx="11" cy="11" r="10" fill="#fff"/><circle cx="11" cy="11" r="7.5" fill="none" stroke="var(--blue)" stroke-width="2"/><path d="M11,6.5 V11 H14" stroke="var(--navy)" stroke-width="1.6" fill="none"/></svg>
      8:30 a.m. – 4:00 p.m
    </div>
    <ul class="card-list" style="top:50px">
      <li><svg width="12" height="11" viewBox="0 0 12 11"><path d="M1,6 l3.5,3.5 l6.5,-8" stroke="#111" stroke-width="2" fill="none"/></svg>Tour of selected programs at NCC</li>
      <li><svg width="12" height="11" viewBox="0 0 12 11"><path d="M1,6 l3.5,3.5 l6.5,-8" stroke="#111" stroke-width="2" fill="none"/></svg>College Career Program overview</li>
      <li><svg width="12" height="11" viewBox="0 0 12 11"><path d="M1,6 l3.5,3.5 l6.5,-8" stroke="#111" stroke-width="2" fill="none"/></svg>Lunch at Brenvale Career and College<br>Academy</li>
      <li><svg width="12" height="11" viewBox="0 0 12 11"><path d="M1,6 l3.5,3.5 l6.5,-8" stroke="#111" stroke-width="2" fill="none"/></svg>Tour of BCCA</li>
      <li><svg width="12" height="11" viewBox="0 0 12 11"><path d="M1,6 l3.5,3.5 l6.5,-8" stroke="#111" stroke-width="2" fill="none"/></svg>Overview of CTE program paths</li>
    </ul>
  </div>

  <!-- Future Technologies -->
  <div class="card" style="left:383px;top:273px;height:136px">
    <div class="card-date" style="top:-6px">March 14</div>
    <div class="card-title" style="top:2px">Future Technologies &amp;<br>Communications</div>
    <div class="card-time" style="top:41px">
      <svg width="22" height="22" viewBox="0 0 22 22"><circle cx="11" cy="11" r="10" fill="#fff"/><circle cx="11" cy="11" r="7.5" fill="none" stroke="var(--blue)" stroke-width="2"/><path d="M11,6.5 V11 H14" stroke="var(--navy)" stroke-width="1.6" fill="none"/></svg>
      8:30 a.m. – 4:00 p.m
    </div>
    <ul class="card-list" style="top:72px">
      <li><svg width="12" height="11" viewBox="0 0 12 11"><path d="M1,6 l3.5,3.5 l6.5,-8" stroke="#111" stroke-width="2" fill="none"/></svg>NCC Presents interview</li>
      <li><svg width="12" height="11" viewBox="0 0 12 11"><path d="M1,6 l3.5,3.5 l6.5,-8" stroke="#111" stroke-width="2" fill="none"/></svg>Trends and forecasts</li>
      <li><svg width="12" height="11" viewBox="0 0 12 11"><path d="M1,6 l3.5,3.5 l6.5,-8" stroke="#111" stroke-width="2" fill="none"/></svg>Marketing &amp; communications panel</li>
    </ul>
  </div>

  <!-- Government -->
  <div class="card" style="left:383px;top:425px;height:153px">
    <div class="card-date" style="top:-5px;font-size:12px">April 4</div>
    <div class="card-title" style="top:2px">Government</div>
    <div class="card-time" style="top:21px">
      <svg width="22" height="22" viewBox="0 0 22 22"><circle cx="11" cy="11" r="10" fill="#fff"/><circle cx="11" cy="11" r="7.5" fill="none" stroke="var(--blue)" stroke-width="2"/><path d="M11,6.5 V11 H14" stroke="var(--navy)" stroke-width="1.6" fill="none"/></svg>
      8:30 a.m. – 4:00 p.m
    </div>
    <ul class="card-list" style="top:53px">
      <li><svg width="12" height="11" viewBox="0 0 12 11"><path d="M1,6 l3.5,3.5 l6.5,-8" stroke="#111" stroke-width="2" fill="none"/></svg>Overview of state/federal government</li>
      <li><svg width="12" height="11" viewBox="0 0 12 11"><path d="M1,6 l3.5,3.5 l6.5,-8" stroke="#111" stroke-width="2" fill="none"/></svg>Overview of city/county government</li>
      <li><svg width="12" height="11" viewBox="0 0 12 11"><path d="M1,6 l3.5,3.5 l6.5,-8" stroke="#111" stroke-width="2" fill="none"/></svg>Tour of Marlow Ridge Correctional Institute</li>
      <li><svg width="12" height="11" viewBox="0 0 12 11"><path d="M1,6 l3.5,3.5 l6.5,-8" stroke="#111" stroke-width="2" fill="none"/></svg>Tour of courthouse</li>
      <li><svg width="12" height="11" viewBox="0 0 12 11"><path d="M1,6 l3.5,3.5 l6.5,-8" stroke="#111" stroke-width="2" fill="none"/></svg>Judicial presentations</li>
    </ul>
  </div>

  <!-- Health & Wellness -->
  <div class="card" style="left:383px;top:598px;height:162px">
    <div class="card-date" style="top:-5px">May2</div>
    <div class="card-title" style="top:2px">Health &amp; Wellness</div>
    <div class="card-time" style="top:21px">
      <svg width="22" height="22" viewBox="0 0 22 22"><circle cx="11" cy="11" r="10" fill="#fff"/><circle cx="11" cy="11" r="7.5" fill="none" stroke="var(--blue)" stroke-width="2"/><path d="M11,6.5 V11 H14" stroke="var(--navy)" stroke-width="1.6" fill="none"/></svg>
      8:30 a.m. – 4:00 p.m
    </div>
    <ul class="card-list" style="top:53px">
      <li><svg width="12" height="11" viewBox="0 0 12 11"><path d="M1,6 l3.5,3.5 l6.5,-8" stroke="#111" stroke-width="2" fill="none"/></svg>Tour of Lower Ashwater Hospice</li>
      <li><svg width="12" height="11" viewBox="0 0 12 11"><path d="M1,6 l3.5,3.5 l6.5,-8" stroke="#111" stroke-width="2" fill="none"/></svg>Community Wellness Roundtable</li>
      <li><svg width="12" height="11" viewBox="0 0 12 11"><path d="M1,6 l3.5,3.5 l6.5,-8" stroke="#111" stroke-width="2" fill="none"/></svg>Tour of Halvern Cancer Care Center</li>
      <li><svg width="12" height="11" viewBox="0 0 12 11"><path d="M1,6 l3.5,3.5 l6.5,-8" stroke="#111" stroke-width="2" fill="none"/></svg>Virtual Medicine Tutorial</li>
      <li><svg width="12" height="11" viewBox="0 0 12 11"><path d="M1,6 l3.5,3.5 l6.5,-8" stroke="#111" stroke-width="2" fill="none"/></svg>Tour of BRHS</li>
    </ul>
  </div>

  <!-- Graduation -->
  <div class="card" style="left:720px;top:86px;height:139px">
    <div class="card-date" style="top:-4px">May 18</div>
    <div class="card-title" style="top:2px">Graduation Ceremony and<br>Luncheon</div>
    <div class="card-time" style="top:41px;left:19px">
      <svg width="22" height="22" viewBox="0 0 22 22"><circle cx="11" cy="11" r="10" fill="#fff"/><circle cx="11" cy="11" r="7.5" fill="none" stroke="var(--blue)" stroke-width="2"/><path d="M11,6.5 V11 H14" stroke="var(--navy)" stroke-width="1.6" fill="none"/></svg>
      12:00 p.m.
    </div>
    <ul class="card-list" style="top:72px;left:19px;width:250px">
      <li><svg width="12" height="11" viewBox="0 0 12 11"><path d="M1,6 l3.5,3.5 l6.5,-8" stroke="#fff" stroke-width="2" fill="none"/></svg>Participants are encouraged to invite their employer/supervisor/mentor/special guest (x2)</li>
    </ul>
  </div>

  <h3 class="side-head" style="top:240px">Attendance Policy</h3>
  <p class="side-text body-text" style="top:258px">Attendance at all sessions including the opening retreat is compulsory.&nbsp; Participants may miss no more than one session to graduate; however, the Organizational Retreat is mandatory.</p>

  <h3 class="side-head" style="top:350px">Tuition</h3>
  <p class="side-text body-text" style="top:368px">If accepted in the Leadership Brenvale program, you or your employer/sponsor will be invoiced $400 for Chamber members and $500 for non-members.&nbsp; This fee covers costs for the retreat, classroom sessions, lunches, and graduation.&nbsp; No refunds will be provided for participants who drop out of the program or do not fulfill the required curriculum.</p>

  <h3 class="side-head" style="top:516px">To Apply</h3>
  <p class="side-text body-text" style="top:534px">Applications are available on the Chamber’s website, www.TheBrenvaleChamber.com Applications are due by November 2, 2020.<br>Class size is limited.&nbsp; All applications received by the deadline will be reviewed and final participants for the Leadership Brenvale class will be contacted on December 4, 2020.&nbsp; However, all applicants will be notified of the status of their application in writing.</p>

  <p class="abs phone">For questions, please call the Chamber</p>
  <p class="abs phone-num">
    <svg width="15" height="15" viewBox="0 0 15 15"><circle cx="7.5" cy="7.5" r="6.5" fill="none" stroke="var(--navy)" stroke-width="1.4"/><path d="M5,4 l1.3,1.6 l-.8,1 q1,1.8 2.6,2.6 l1,-.8 l1.6,1.3 l-.9,1 q-3.6,-.4 -5.6,-5.4 Z" fill="var(--navy)"/></svg>
    555-014-2738
  </p>
</div>
</body>
</html>
```